Business Card Design for Harbor Restoration - Property Restoration Professionals

I need a business card designed for Harbor Restoration. We are a full-service property restoration solution. Providing water, fire, smoke & storm restoration as well as mold remediation and full remodel or reconstruction to homes and businesses across Dallas-Fort Worth, TX.
Target Market(s)
home and business owners with insurance covered property damage from water, fire or storm related damage
Industry/Entity Type
property restoration
Contact Information for Business Card
Martin Kell General Manager Cell: 214-555-0193 Office: 469-555-0148 email: Martin@HarborRestore.example services: Water, Fire, Mold, Reconstruction Tagline: Fast Help When Water Strikes!
Look and feel
Each slider illustrates characteristics of the customer's brand and the style your logo design should communicate.

```html
<!DOCTYPE html>
<html lang="en">
<head>
<meta charset="utf-8">
<title>Harbor Restoration – Business Card</title>
<link rel="stylesheet" href="https://fonts.googleapis.com/css2?family=Montserrat:wght@700;800&family=Lato:wght@400;700&display=swap">
<style>
  :root {
    --bg: #2a2a2a;
    --card-dark: #1f1f20;
    --brand-blue: #00b2e6;
    --brand-grey: #6d6e70;
    --white: #ffffff;
  }
  * { margin: 0; padding: 0; box-sizing: border-box; }
  html, body { width: 1200px; height: 875px; overflow: hidden; }
  body {
    background: var(--bg);
    display: flex;
    align-items: center;
    justify-content: center;
    gap: 40px;
    font-family: "Lato", sans-serif;
  }
  .card {
    width: 540px;
    height: 309px;
    border-radius: 18px;
    position: relative;
    overflow: hidden;
    box-shadow: 0 12px 30px rgba(0,0,0,.45);
  }

  /* Back side */
  .card-back {
    background: var(--card-dark);
    display: flex;
    flex-direction: column;
    align-items: center;
    justify-content: center;
    text-align: center;
  }
  .brand-mark {
    display: flex;
    align-items: center;
    gap: 12px;
    margin-bottom: 34px;
  }
  .brand-dot {
    width: 22px; height: 22px;
    border-radius: 50%;
    background: var(--brand-blue);
  }
  .brand-name {
    font-family: "Montserrat", sans-serif;
    font-weight: 800;
    font-size: 30px;
    color: var(--brand-blue);
    letter-spacing: .5px;
  }
  .tagline {
    font-family: "Montserrat", sans-serif;
    font-weight: 800;
    font-size: 20px;
    letter-spacing: 1.5px;
    color: var(--brand-blue);
    text-transform: uppercase;
  }
  .services {
    margin-top: 8px;
    font-family: "Montserrat", sans-serif;
    font-weight: 700;
    font-size: 13px;
    letter-spacing: 3px;
    color: var(--white);
    text-transform: uppercase;
    display: flex;
    align-items: center;
    gap: 8px;
  }
  .drop { width: 8px; height: 11px; }

  /* Front side */
  .card-front { background: var(--brand-blue); }
  .white-disc {
    position: absolute;
    width: 420px; height: 420px;
    border-radius: 50%;
    background: var(--white);
    left: 268px; top: -90px;
  }
  .grey-arc {
    position: absolute;
    left: 258px; top: -100px;
    width: 440px; height: 440px;
  }
  .front-brand {
    position: absolute;
    left: 318px; top: 128px;
    width: 210px;
    font-family: "Montserrat", sans-serif;
    font-weight: 800;
    font-size: 24px;
    line-height: 1.15;
    color: var(--brand-blue);
    text-align: center;
  }
  .person {
    position: absolute;
    left: 30px; top: 42px;
    color: var(--white);
  }
  .person-name {
    font-family: "Montserrat", sans-serif;
    font-weight: 800;
    font-size: 26px;
    text-transform: uppercase;
    letter-spacing: .3px;
  }
  .person-title { font-size: 15px; margin-top: 2px; }
  .contact-list {
    position: absolute;
    left: 30px; bottom: 26px;
    list-style: none;
    color: var(--white);
    font-size: 14px;
    line-height: 22px;
  }
  .contact-list li { display: flex; align-items: center; gap: 10px; }
  .contact-list svg { width: 13px; height: 13px; flex: none; }
</style>
</head>
<body>

  <section class="card card-back" aria-label="Card back">
    <div class="brand-mark">
      <span class="brand-dot"></span>
      <span class="brand-name">Harbor Restoration</span>
    </div>
    <p class="tagline">Fast help when water strikes!</p>
    <p class="services">
      <span>Water</span>
      <svg class="drop" viewBox="0 0 8 11"><path d="M4 0C4 0 0 5 0 7a4 4 0 0 0 8 0C8 5 4 0 4 0z" fill="#00b2e6"/></svg>
      <span>Fire</span>
      <svg class="drop" viewBox="0 0 8 11"><path d="M4 0C4 0 0 5 0 7a4 4 0 0 0 8 0C8 5 4 0 4 0z" fill="#00b2e6"/></svg>
      <span>Mold</span>
      <svg class="drop" viewBox="0 0 8 11"><path d="M4 0C4 0 0 5 0 7a4 4 0 0 0 8 0C8 5 4 0 4 0z" fill="#00b2e6"/></svg>
      <span>Reconstruction</span>
    </p>
  </section>

  <section class="card card-front" aria-label="Card front">
    <div class="white-disc"></div>
    <svg class="grey-arc" viewBox="0 0 440 440" aria-hidden="true">
      <path d="M16 180 A210 210 0 0 0 300 412" fill="none" stroke="#6d6e70" stroke-width="5"/>
    </svg>
    <div class="front-brand">Harbor Restoration</div>

    <div class="person">
      <h1 class="person-name">Martin Kell</h1>
      <p class="person-title">General Manager</p>
    </div>

    <ul class="contact-list">
      <li>
        <svg viewBox="0 0 24 24"><path d="M6.6 10.8a15 15 0 0 0 6.6 6.6l2.2-2.2c.3-.3.7-.4 1-.2 1.1.4 2.3.6 3.6.6.6 0 1 .4 1 1V20c0 .6-.4 1-1 1A17 17 0 0 1 3 4c0-.6.4-1 1-1h3.5c.6 0 1 .4 1 1 0 1.3.2 2.5.6 3.6.1.3 0 .7-.2 1z" fill="#fff"/></svg>
        469-555-0148
      </li>
      <li>
        <svg viewBox="0 0 24 24"><rect x="6" y="2" width="12" height="20" rx="2" fill="none" stroke="#fff" stroke-width="2"/><circle cx="12" cy="18" r="1.3" fill="#fff"/></svg>
        214-555-0193
      </li>
      <li>
        <svg viewBox="0 0 24 24"><rect x="2" y="5" width="20" height="14" rx="1" fill="#fff"/><path d="M2 5l10 8 10-8" fill="none" stroke="#00b2e6" stroke-width="2"/></svg>
        Martin@HarborRestore.example
      </li>
      <li>
        <svg viewBox="0 0 24 24"><circle cx="12" cy="12" r="9" fill="none" stroke="#fff" stroke-width="2"/><path d="M3 12h18M12 3c3 3 3 15 0 18M12 3c-3 3-3 15 0 18" fill="none" stroke="#fff" stroke-width="1.5"/></svg>
        HarborRestore.example
      </li>
    </ul>
  </section>

</body>
</html>
```